Graphic Design Set for Banner Ads - Sizes and Specs for Bidlane

We need a set of 6 ads of the following sizes created for Bidlane:

Medium rectangle: 300×250
Leaderboard: 728×90
Wide skyscraper: 160×600
Large rectangle: 300x600
Mobile leaderboard: 320×50

Here are the Formatting Guidelines (WEB ADS): https://help.bidlane.com/hc/en-us/articles/583920147-Ad-Content-and-Format-Guidelines

Here is the website: https://mavenhollowcare.com/

Here are some words for the ad - feel free to use creative liberties if you have something better or need less words.

1. The Future of Aging is Here

2. Dementia At-Home Care

3. Benefits of an Assisted Living from the Privacy of Your Home - link to

4. Idaho's New Senior Care Option

5. The Security of Senior Living from the Comfort of Your Home

I have the images for all website photos, if you need more images, please let me know.

Target Market(s)

Women age 55+

Industry/Entity Type

Graphic Design

Requirements
Must have
• Incorporate website imagery as much as possible
Should not have
• a feeling of helplessness, old, etc.

```html
<!DOCTYPE html>
<html lang="en">
<head>
<meta charset="utf-8">
<title>Maven Hollow – Banner Ads</title>
<link rel="stylesheet" href="https://fonts.googleapis.com/css2?family=Mulish:wght@600;700&family=Poppins:wght@400&display=swap">
<style>
  :root {
    --navy: #19355d;
    --card: #f6f6f6;
    --ink: #141414;
    --gold-text: #c6b05a;
    --gold-ring: #e6d07e;
    --gold-line: #d2bf72;
    --plum: #4a2438;
    --plum-deep: #471c3c;
  }
  html, body {
    margin: 0;
    width: 1200px;
    height: 1200px;
    overflow: hidden;
    background: var(--navy);
  }
  .ad-set {
    position: relative;
    width: 1200px;
    height: 1200px;
  }
  .ad-card {
    position: absolute;
    top: 103px;
    width: 494px;
    height: 988px;
    background: var(--card);
    overflow: hidden;
  }
  .ad-card--portrait { left: 72px; }
  .ad-card--garden { left: 632px; }

  .brand {
    position: absolute;
    top: 72px;
    left: 0;
    width: 100%;
    display: flex;
    align-items: center;
    justify-content: center;
    gap: 12px;
  }
  .brand-dot {
    width: 18px;
    height: 18px;
    border-radius: 50%;
    background: var(--gold-text);
  }
  .brand-name {
    font-family: "Poppins", sans-serif;
    font-weight: 400;
    font-size: 46px;
    letter-spacing: 1px;
    color: var(--ink);
    line-height: 1;
  }

  .tagline {
    position: absolute;
    top: 190px;
    left: 0;
    width: 100%;
    margin: 0;
    text-align: center;
    font-family: "Mulish", sans-serif;
    font-weight: 700;
    font-size: 25px;
    line-height: 37px;
    color: var(--gold-text);
    text-transform: uppercase;
  }

  .photo {
    position: absolute;
    left: 22px;
    top: 290px;
    width: 472px;
    height: 472px;
    border-radius: 50%;
  }
  .ad-card--portrait .photo {
    background: radial-gradient(circle at 50% 42%, #f2d9c4 0%, #e9c7a8 24%, #c99a3a 52%, #b8862a 70%, #3a63b8 100%);
  }
  .ad-card--garden .photo {
    background: radial-gradient(circle at 45% 60%, #bdb8b0 0%, #a89a86 28%, #6f8a4c 58%, #4f6f34 80%, #d8d4cc 100%);
  }
  .ring {
    position: absolute;
    left: 0;
    top: 0;
    width: 494px;
    height: 988px;
    pointer-events: none;
  }

  .offer {
    position: absolute;
    top: 800px;
    left: 0;
    width: 100%;
    margin: 0;
    text-align: center;
    font-family: "Mulish", sans-serif;
    font-weight: 600;
    font-size: 25px;
    line-height: 37px;
    color: var(--plum);
  }

  .cta {
    position: absolute;
    left: 152px;
    top: 906px;
    width: 194px;
    height: 54px;
    box-sizing: border-box;
    border: 3px solid var(--gold-line);
    display: flex;
    align-items: center;
    justify-content: center;
    font-family: "Mulish", sans-serif;
    font-weight: 700;
    font-size: 24px;
    color: var(--plum-deep);
    text-decoration: none;
  }
</style>
</head>
<body>
<main class="ad-set">

  <article class="ad-card ad-card--portrait">
    <div class="brand">
      <span class="brand-name">Maven Hollow</span>
      <span class="brand-dot"></span>
    </div>
    <h2 class="tagline">Live your life and<br>forget the age</h2>
    <div class="photo" role="img" aria-label="Photo of a smiling senior woman with white hair and glasses, warm golden background"></div>
    <svg class="ring" viewBox="0 0 494 988" aria-hidden="true">
      <circle cx="258" cy="526" r="244" fill="none" stroke="var(--gold-ring)" stroke-width="11"/>
      <circle cx="46" cy="435" r="17" fill="var(--card)" stroke="var(--gold-ring)" stroke-width="10"/>
      <circle cx="46" cy="617" r="17" fill="var(--card)" stroke="var(--gold-ring)" stroke-width="10"/>
    </svg>
    <p class="offer">Assisted Home Care for<br>Senior Living</p>
    <a class="cta" href="https://mavenhollowcare.com/">Hire Us</a>
  </article>

  <article class="ad-card ad-card--garden">
    <div class="brand">
      <span class="brand-name">Maven Hollow</span>
      <span class="brand-dot"></span>
    </div>
    <h2 class="tagline">Live your life and<br>forget the age</h2>
    <div class="photo" role="img" aria-label="Photo of a senior woman relaxing in a garden chair beside a curly white dog, with rose bushes behind"></div>
    <svg class="ring" viewBox="0 0 494 988" aria-hidden="true">
      <circle cx="258" cy="526" r="244" fill="none" stroke="var(--gold-ring)" stroke-width="11"/>
      <circle cx="46" cy="435" r="17" fill="var(--card)" stroke="var(--gold-ring)" stroke-width="10"/>
      <circle cx="46" cy="617" r="17" fill="var(--card)" stroke="var(--gold-ring)" stroke-width="10"/>
    </svg>
    <p class="offer">Assisted Home Care for<br>Senior Living</p>
    <a class="cta" href="https://mavenhollowcare.com/">Hire Us</a>
  </article>

</main>
</body>
</html>
```